Brightwater Court Services needs a business card

I need a business card design for a new company
For the last 10 years I have ran a tennis management company called Silver Hollow Racquet (www.silverhollowracquet.com)
The new company - Brightwater Court Services (BCS) will replace SHRA starting this winter
The goal of BCS will be to expand our operations into new clubs as well and a revenue stream from existing clubs with courtlinkhub.net
We plan to go regional in 2014 and then look outward from there

Target Market(s)

small to medium sized tennis facilities both public and private
Our market are the clubs - not the players
This includes private clubs, municipalities, recreation assc, etc

Industry/Entity Type

Business

Requirements
Must have
• Dale Huxley
• President
• 555-284-1937 Office
• 555-419-5062 Cell
• dhuxley@brightwatercourtservices.com
• www.brightwatercourtservices.com
Nice to have
• One of the unique benefits to a company joining BCS will be integration into our web based club software service - Courtlinkhub.net
• We have developed this turnkey service for small to medium sized clubs and re the exclusive providers of it
Should not have
• address or state

```html
<!DOCTYPE html>
<html lang="en">
<head>
<meta charset="utf-8">
<title>Brightwater Court Services – Business Card</title>
<link rel="stylesheet" href="https://fonts.googleapis.com/css2?family=Arimo:wght@400;700&display=swap">
<style>
  :root {
    --page-bg: #ffffff;
    --card-black: #1e1c1c;
    --grey-light: #f4f4f4;
    --grey-mid: #bdbdbd;
    --grey-dark: #7d7d7d;
    --brand-white: #ffffff;
    --ball-yellow: #f2c40f;
    --ink: #111111;
    --ink-soft: #2a2a2a;
  }
  html, body {
    margin: 0;
    padding: 0;
    width: 1200px;
    height: 1000px;
    overflow: hidden;
    background: var(--page-bg);
  }
  .canvas {
    position: relative;
    width: 1200px;
    height: 1000px;
  }
  .card {
    position: absolute;
    top: 328px;
    width: 540px;
    height: 345px;
    overflow: hidden;
  }
  .card--front { left: 50px; }
  .card--back  { left: 610px; }

  .card__surface {
    position: absolute;
    inset: 0;
    background: radial-gradient(ellipse at center, var(--grey-light) 0%, var(--grey-mid) 55%, var(--grey-dark) 100%);
  }
  .card__shape {
    position: absolute;
    inset: 0;
    width: 100%;
    height: 100%;
  }
  .brand {
    position: absolute;
    left: 0;
    right: 0;
    top: 150px;
    display: flex;
    align-items: center;
    justify-content: center;
    gap: 14px;
  }
  .brand__name {
    font-family: "Arimo", Arial, sans-serif;
    font-weight: 400;
    font-size: 34px;
    color: var(--brand-white);
    letter-spacing: -0.5px;
  }
  .brand__dot {
    width: 22px;
    height: 22px;
    border-radius: 50%;
    background: var(--ball-yellow);
  }

  .back-content {
    position: absolute;
    left: 0;
    right: 0;
    top: 130px;
    display: flex;
    flex-direction: column;
    align-items: center;
    font-family: "Arimo", Arial, sans-serif;
    color: var(--ink);
    text-align: center;
  }
  .website {
    margin: 0 0 26px;
    font-weight: 700;
    font-size: 19px;
  }
  .contact {
    margin: 0;
    font-style: normal;
    display: flex;
    flex-direction: column;
    align-items: center;
    gap: 4px;
  }
  .contact__name {
    font-weight: 700;
    font-size: 18px;
  }
  .contact__title {
    font-weight: 400;
    font-size: 15px;
    color: var(--ink-soft);
    margin-bottom: 8px;
  }
  .contact__line {
    font-weight: 400;
    font-size: 15px;
    color: var(--ink-soft);
  }
</style>
</head>
<body>
<main class="canvas">
  <section class="card card--front" aria-label="Card front">
    <div class="card__surface"></div>
    <svg class="card__shape" viewBox="0 0 414 265" preserveAspectRatio="none" aria-hidden="true">
      <rect x="0" y="58" width="414" height="152" fill="var(--card-black)"/>
      <ellipse cx="207" cy="133" rx="150" ry="98" fill="var(--card-black)"/>
    </svg>
    <div class="brand">
      <span class="brand__name">courtlinkhub</span>
      <span class="brand__dot"></span>
    </div>
  </section>

  <section class="card card--back" aria-label="Card back">
    <div class="card__surface"></div>
    <div class="back-content">
      <p class="website">www.brightwatercourtservices.com</p>
      <address class="contact">
        <span class="contact__name">Dale Huxley</span>
        <span class="contact__title">President</span>
        <span class="contact__line">555-284-1937 Office</span>
        <span class="contact__line">555-419-5062 Cell</span>
        <span class="contact__line">dhuxley@brightwatercourtservices.com</span>
      </address>
    </div>
  </section>
</main>
</body>
</html>
```